Funky new Serviced Apartment Company needs a website + logo

Bright Nest Serviced Accommodation is a new company aiming to attract customers who need temporary accommodation (2 days to 6 months) in city locations.

Our customers make considerable savings on longer stays compared to hotels, and have all the creature comforts of home including super-fast WIFI, comfy beds, full kitchen and modern, yet comfortable, furniture.

Another key feature of the design is a page to attract "Partners" who "Work with Us" by allowing us to manage their properties and becoming part of our network of accommodation units. I have include a brochure from one of our competitors, and a video can be found here: http://lnkvault-example.com/aptclip-7 - both can be used as I have permission.

The website design should work on all devices and screen sizes, and lend itself to a mobile app.

We would like to see website designs that are modern and simple, with a strong brand logo. The final design should communicate "Home From Home" and aim to attract professionals away from home on business for long periods of time.

Target Market(s)

Professional People working away from home for extended periods of time

Industry/Entity Type

Accommodation

Contact Information for Business Card

Name, Title, Phone Number, Email
Callum Fenwick, Owner, 07831 552907, callum.fenwick@brightnestsa-example.co.uk

Logo Text

Bright Nest Service Accommodation (Serviced Accommodation optional)

Coding

Coded - Design and coding required

Number of Pages Required

3 page

Font styles to use
Sans Serif

Requirements
Must have
• A 3 page website: Home, Partners, Contact Us
• Home page should have an area to list current apartment units, the user should be able to select a location and filter the list based on price and number of people.
• Partners page should inspire a "Work with us" call to action.
• The design should work with all screen sizes and devices.
• The design should say friendly and professional
Nice to have
• A simple logo, perhaps a smiling face made up using letters 'W' and 'H'.
• A neutral color scheme
Should not have
• No garish or vivid color scheme

```html
<!DOCTYPE html>
<html lang="en">
<head>
<meta charset="utf-8">
<title>Bright Nest Serviced Accommodation</title>
<link rel="stylesheet" href="https://fonts.googleapis.com/css2?family=PT+Sans:wght@400;700&family=Signika:wght@300;400;600&display=swap">
<style>
:root{
  --gold:#b3a36a;
  --gold-dark:#9c8c55;
  --olive-band:#8f866c;
  --ink:#3b3b3b;
  --muted:#8a8a8a;
  --line:#d9d4c2;
  --card:#f6f6f4;
  --pill:#5a5a5a;
  --footer:#a6985f;
  --footer-dark:#958852;
  --white:#ffffff;
}
*{box-sizing:border-box;margin:0;padding:0}
html,body{width:1200px;height:4878px;overflow:hidden}
body{font-family:"PT Sans",Arial,sans-serif;color:var(--ink);background:var(--white);position:relative}
section,header,footer{position:absolute;left:0;width:1200px}

/* header */
.site-header{top:0;height:97px;background:var(--white);display:flex;align-items:center;justify-content:space-between;padding:0 125px 0 127px}
.brand{display:flex;align-items:center;gap:12px}
.brand-mark{width:26px;height:26px;background:var(--gold)}
.brand-name{font-family:"Signika",sans-serif;font-weight:600;font-size:24px;color:var(--gold)}
.main-nav{display:flex;gap:32px;font-size:13px;font-weight:700;color:var(--ink);text-transform:uppercase}
.main-nav a{text-decoration:none;color:inherit;padding-bottom:6px}
.main-nav a.active{border-bottom:2px solid var(--ink)}

/* hero */
.hero{top:97px;height:463px;background:linear-gradient(180deg,#8d7a62 0%,#6f5c47 45%,#4d3c2e 100%)}
.hero-photo{position:absolute;inset:0;background:radial-gradient(ellipse at 70% 40%,rgba(220,205,180,.55),transparent 60%),linear-gradient(90deg,rgba(60,45,35,.6),rgba(140,120,95,.2) 50%,rgba(60,45,35,.5))}
.hero-title{position:absolute;top:186px;width:100%;text-align:center;font-family:"Signika",sans-serif;font-weight:300;font-size:35px;line-height:44px;color:var(--white);text-transform:uppercase;letter-spacing:.5px}
.search-bar{position:absolute;top:309px;left:126px;width:962px;height:70px;background:rgba(25,20,15,.75);display:flex;align-items:center;gap:18px;padding:0 18px}
.search-select{height:42px;width:250px;background:rgba(0,0,0,.55);border:1px solid rgba(255,255,255,.15);color:#ddd;font-size:11px;text-transform:uppercase;display:flex;align-items:center;justify-content:space-between;padding:0 14px}
.search-select svg{width:10px;height:10px}
.search-btn{margin-left:auto;height:42px;width:120px;background:var(--gold);color:var(--white);font-weight:700;font-size:14px;display:flex;align-items:center;justify-content:center;text-transform:uppercase}

/* amenities band */
.amenity-band{top:560px;height:84px;background:var(--olive-band);display:flex;justify-content:center;gap:88px;align-items:center}
.amenity{display:flex;align-items:center;gap:12px;color:var(--white);font-weight:700;font-size:15px;text-transform:uppercase}
.amenity svg{width:34px;height:28px}

.section-title{position:absolute;width:100%;text-align:center;font-family:"Signika",sans-serif;font-weight:600;font-size:24px;color:var(--gold);text-transform:uppercase}

/* listings */
.listings{top:644px;height:1525px}
.listings .section-title{top:76px}
.listing{position:absolute;left:143px;width:914px;height:283px;background:var(--card);display:flex}
.listing-photo{width:289px;height:283px;flex:none}
.listing-body{flex:1;padding:24px 14px 0 24px;position:relative}
.listing-title{font-family:"Signika",sans-serif;font-weight:600;font-size:20px;color:var(--ink)}
.location{font-size:11px;color:var(--muted);margin-top:4px}
.location b{color:var(--ink)}
.listing-actions{position:absolute;top:24px;right:14px;display:flex;gap:8px;align-items:center}
.people-pill{background:var(--pill);color:var(--white);font-size:11px;font-weight:700;border-radius:14px;padding:6px 12px;display:flex;align-items:center;gap:6px}
.people-pill span{background:var(--gold);border-radius:3px;padding:1px 5px;font-size:10px}
.icon-btn{width:28px;height:26px;background:var(--gold);display:flex;align-items:center;justify-content:center}
.icon-btn.light{background:#c9c3b0}
.icon-btn svg{width:13px;height:13px}
.dash{border-top:1px dashed var(--line);margin:12px 0}
.excerpt{font-size:11px;line-height:17px;color:var(--muted);width:560px}
.price{font-weight:700;font-size:16px;margin-top:18px}
.tag-btn{display:inline-block;background:var(--gold);color:var(--white);font-size:8px;text-transform:uppercase;padding:4px 12px;margin-top:8px}
.amenity-row{display:flex;gap:62px;font-size:9px;color:var(--muted);text-transform:uppercase}
.amenity-row span{display:flex;align-items:center;gap:8px}
.amenity-row svg{width:18px;height:14px}
.more-btn{position:absolute;top:1365px;left:462px;width:276px;height:46px;background:var(--gold);color:var(--white);font-weight:700;font-size:14px;text-transform:uppercase;border-radius:6px;display:flex;align-items:center;justify-content:center}

/* video */
.video-band{top:2169px;height:540px;background:linear-gradient(120deg,#4a3b2e,#6e5a45 50%,#3e3126)}
.video-frame{position:absolute;top:107px;left:202px;width:796px;height:335px;border:5px solid var(--white);background:linear-gradient(135deg,#6a5a9a,#54437f 55%,#3c2f62)}
.video-frame p{position:absolute;top:115px;width:100%;text-align:center;font-family:"Signika",sans-serif;font-weight:300;color:var(--white);font-size:52px;line-height:52px;text-transform:uppercase}
.play{position:absolute;top:132px;left:368px;width:60px;height:60px}

/* featured */
.featured{top:2709px;height:1343px}
.featured .section-title{top:104px}
.feature-card{position:absolute;width:290px;height:507px;background:var(--card)}
.feature-photo{height:207px;position:relative}
.feature-photo .icons{position:absolute;top:14px;right:12px;display:flex;gap:6px}
.feature-body{padding:20px 20px 0}
.feature-body .listing-title{font-size:19px}
.feature-body .excerpt{width:auto;margin-top:12px}
.feature-body .price{margin-top:10px;font-size:15px}
.details-btn{display:inline-block;margin-top:18px;background:var(--gold);color:var(--white);font-weight:700;font-size:11px;text-transform:uppercase;padding:9px 18px;border-radius:5px}
.scroll-down{position:absolute;top:1276px;left:578px;width:44px;height:44px;border-radius:50%;border:1px solid #bbb;display:flex;align-items:center;justify-content:center}

/* testimonials */
.testimonials{top:4052px;height:465px;background:linear-gradient(180deg,#a39863,#978b58)}
.testimonials .section-title{top:70px;color:var(--white)}
.guest-photo{position:absolute;top:154px;left:238px;width:226px;height:226px;border-radius:50%;border:6px solid var(--white);background:linear-gradient(180deg,#7d9bb8,#9aa77a 60%,#5f6b45)}
.quote{position:absolute;top:200px;left:478px;width:560px;color:var(--white);font-size:18px;line-height:28px}
.guest{position:absolute;top:298px;left:478px;color:var(--white)}
.guest strong{font-family:"Signika",sans-serif;font-size:20px;display:block}
.guest span{font-size:13px}

/* footer */
.site-footer{top:4517px;height:289px;background:var(--footer);color:var(--white);padding:48px 0 0 127px;display:flex}
.footer-col{font-size:11px;line-height:17px}
.footer-about{width:373px}
.footer-about .brand-name{color:var(--white);font-size:30px}
.footer-about p{margin-top:18px;width:235px}
.read-more{display:inline-block;margin-top:16px;background:var(--footer-dark);font-size:9px;font-weight:700;padding:5px 12px;text-transform:uppercase}
.footer-col h4{font-family:"Signika",sans-serif;font-size:15px;font-weight:600;margin-bottom:18px}
.footer-links{width:225px}
.footer-contact{width:250px}
.contact-line{display:flex;gap:10px;margin-bottom:14px;white-space:nowrap}
.contact-line svg{width:13px;height:13px;flex:none;margin-top:2px}
.bottom-bar{top:4806px;height:72px;background:var(--footer-dark);color:var(--white);font-size:11px;font-weight:700;display:flex;align-items:center;justify-content:space-between;padding:0 38px 0 127px}
.socials{display:flex;gap:12px}
.socials i{width:10px;height:10px;border-radius:50%;background:rgba(255,255,255,.8);display:block}
</style>
</head>
<body>

<header class="site-header">
  <div class="brand"><span class="brand-mark"></span><span class="brand-name">Bright Nest</span></div>
  <nav class="main-nav">
    <a class="active">Home</a><a>About Us</a><a>Accomadation</a><a>Our Customers</a><a>Contact Us</a>
  </nav>
</header>

<section class="hero">
  <div class="hero-photo" role="img" aria-label="Photo of a bright, modern serviced apartment bedroom with sofa and large windows"></div>
  <h1 class="hero-title">Bright Nest Serviced<br>Accommodation</h1>
  <div class="search-bar">
    <div class="search-select">Select your location <svg viewBox="0 0 10 10"><path d="M1 3l4 4 4-4" stroke="#ddd" fill="none"/></svg></div>
    <div class="search-select">Price range <svg viewBox="0 0 10 10"><path d="M1 3l4 4 4-4" stroke="#ddd" fill="none"/></svg></div>
    <div class="search-select">Peoples <svg viewBox="0 0 10 10"><path d="M1 3l4 4 4-4" stroke="#ddd" fill="none"/></svg></div>
    <div class="search-btn">Search</div>
  </div>
</section>

<section class="amenity-band">
  <div class="amenity"><svg viewBox="0 0 34 28" fill="none" stroke="#fff" stroke-width="2"><rect x="3" y="3" width="28" height="18" rx="2"/><path d="M12 12a7 7 0 0 1 10 0M14.5 15a3.5 3.5 0 0 1 5 0"/><path d="M9 25h16"/></svg>Super-fast wifi</div>
  <div class="amenity"><svg viewBox="0 0 34 28" fill="none" stroke="#fff" stroke-width="2"><path d="M3 6v18M3 17h28v7M3 13h28v4M8 13V9h9v4"/></svg>Comfy beds</div>
  <div class="amenity"><svg viewBox="0 0 34 28" fill="none" stroke="#fff" stroke-width="2"><path d="M6 12h22v10a3 3 0 0 1-3 3H9a3 3 0 0 1-3-3zM3 12h28M12 8c0-3 10-3 10 0"/></svg>Full kitchen</div>
  <div class="amenity"><svg viewBox="0 0 34 28" fill="none" stroke="#fff" stroke-width="2"><path d="M8 14V6a3 3 0 0 1 3-3h12a3 3 0 0 1 3 3v8M4 14h26v7H4zM7 21v4M27 21v4"/></svg>Furniture</div>
</section>

<section class="listings">
  <h2 class="section-title">Our Current Listings</h2>

  <article class="listing" style="top:160px">
    <div class="listing-photo" role="img" aria-label="Photo of a bright bedroom with pendant lights" style="background:linear-gradient(135deg,#d8d1c4,#b19c82 60%,#7d6650)"></div>
    <div class="listing-body">
      <h3 class="listing-title">Johnson Apartment</h3>
      <p class="location"><b>Location :</b> New Jersey | USA</p>
      <div class="listing-actions"><div class="people-pill">People Accomodated : <span>10</span></div><div class="icon-btn"><svg viewBox="0 0 13 13"><path d="M6.5 11L2 6.5a2.5 2.5 0 0 1 4.5-3 2.5 2.5 0 0 1 4.5 3z" fill="#fff"/></svg></div><div class="icon-btn light"><svg viewBox="0 0 13 13"><path d="M2 7l4 4 5-9" stroke="#fff" stroke-width="2" fill="none"/></svg></div></div>
      <div class="dash"></div>
      <p class="excerpt">Lorem ipsum dolor sit amet, consectetur adipiscing elit, sed do eiusmod tempor incididunt ut labore et dolore magna aliqua. Ut enim ad minim veniam, quis nostrud exercitation.</p>
      <p class="price">PRICE : $1,25,000</p>
      <span class="tag-btn">View location</span>
      <div class="dash"></div>
      <div class="amenity-row">
        <span><svg viewBox="0 0 18 14" fill="none" stroke="#999" stroke-width="1.5"><rect x="1" y="1" width="16" height="10"/><path d="M6 7a4 4 0 0 1 6 0"/></svg>Super-fast wifi</span>
        <span><svg viewBox="0 0 18 14" fill="none" stroke="#999" stroke-width="1.5"><path d="M1 2v11M1 9h16v4M1 6h16v3"/></svg>Comfy beds</span>
        <span><svg viewBox="0 0 18 14" fill="none" stroke="#999" stroke-width="1.5"><path d="M3 6h12v6H3zM1 6h16"/></svg>Full kitchen</span>
        <span><svg viewBox="0 0 18 14" fill="none" stroke="#999" stroke-width="1.5"><path d="M4 7V2h10v5M2 7h14v4H2z"/></svg>Furniture</span>
      </div>
    </div>
  </article>

  <article class="listing" style="top:450px">
    <div class="listing-photo" role="img" aria-label="Photo of a dark-toned bedroom with a large bed" style="background:linear-gradient(135deg,#3c3531,#5a4d45 55%,#8b7d70)"></div>
    <div class="listing-body">
      <h3 class="listing-title">Johnson Apartment</h3>
      <p class="location"><b>Location :</b> New Jersey | USA</p>
      <div class="listing-actions"><div class="people-pill">People Accomodated : <span>10</span></div><div class="icon-btn"><svg viewBox="0 0 13 13"><path d="M6.5 11L2 6.5a2.5 2.5 0 0 1 4.5-3 2.5 2.5 0 0 1 4.5 3z" fill="#fff"/></svg></div><div class="icon-btn light"><svg viewBox="0 0 13 13"><path d="M2 7l4 4 5-9" stroke="#fff" stroke-width="2" fill="none"/></svg></div></div>
      <div class="dash"></div>
      <p class="excerpt">Lorem ipsum dolor sit amet, consectetur adipiscing elit, sed do eiusmod tempor incididunt ut labore et dolore magna aliqua. Ut enim ad minim veniam, quis nostrud exercitation.</p>
      <p class="price">PRICE : $145,000</p>
      <span class="tag-btn">View location</span>
      <div class="dash"></div>
      <div class="amenity-row">
        <span><svg viewBox="0 0 18 14" fill="none" stroke="#999" stroke-width="1.5"><rect x="1" y="1" width="16" height="10"/><path d="M6 7a4 4 0 0 1 6 0"/></svg>Super-fast wifi</span>
        <span><svg viewBox="0 0 18 14" fill="none" stroke="#999" stroke-width="1.5"><path d="M1 2v11M1 9h16v4M1 6h16v3"/></svg>Comfy beds</span>
        <span><svg viewBox="0 0 18 14" fill="none" stroke="#999" stroke-width="1.5"><path d="M3 6h12v6H3zM1 6h16"/></svg>Full kitchen</span>
        <span><svg viewBox="0 0 18 14" fill="none" stroke="#999" stroke-width="1.5"><path d="M4 7V2h10v5M2 7h14v4H2z"/></svg>Furniture</span>
      </div>
    </div>
  </article>

  <article class="listing" style="top:740px">
    <div class="listing-photo" role="img" aria-label="Photo of a bedroom with wooden wall panels" style="background:linear-gradient(135deg,#5e4432,#8a6a50 50%,#c9b8a2)"></div>
    <div class="listing-body">
      <h3 class="listing-title">Johnson Apartment</h3>
      <p class="location"><b>Location :</b> New Jersey | USA</p>
      <div class="listing-actions"><div class="people-pill">People Accomodated : <span>10</span></div><div class="icon-btn"><svg viewBox="0 0 13 13"><path d="M6.5 11L2 6.5a2.5 2.5 0 0 1 4.5-3 2.5 2.5 0 0 1 4.5 3z" fill="#fff"/></svg></div><div class="icon-btn light"><svg viewBox="0 0 13 13"><path d="M2 7l4 4 5-9" stroke="#fff" stroke-width="2" fill="none"/></svg></div></div>
      <div class="dash"></div>
      <p class="excerpt">Lorem ipsum dolor sit amet, consectetur adipiscing elit, sed do eiusmod tempor incididunt ut labore et dolore magna aliqua. Ut enim ad minim veniam, quis nostrud exercitation.</p>
      <p class="price">PRICE : $1,35,000</p>
      <span class="tag-btn">View location</span>
      <div class="dash"></div>
      <div class="amenity-row">
        <span><svg viewBox="0 0 18 14" fill="none" stroke="#999" stroke-width="1.5"><rect x="1" y="1" width="16" height="10"/><path d="M6 7a4 4 0 0 1 6 0"/></svg>Super-fast wifi</span>
        <span><svg viewBox="0 0 18 14" fill="none" stroke="#999" stroke-width="1.5"><path d="M1 2v11M1 9h16v4M1 6h16v3"/></svg>Comfy beds</span>
        <span><svg viewBox="0 0 18 14" fill="none" stroke="#999" stroke-width="1.5"><path d="M3 6h12v6H3zM1 6h16"/></svg>Full kitchen</span>
        <span><svg viewBox="0 0 18 14" fill="none" stroke="#999" stroke-width="1.5"><path d="M4 7V2h10v5M2 7h14v4H2z"/></svg>Furniture</span>
      </div>
    </div>
  </article>

  <article class="listing" style="top:1030px">
    <div class="listing-photo" role="img" aria-label="Photo of a warm bedroom with striped bedding" style="background:linear-gradient(135deg,#a58c72,#6e5540 55%,#d9cbb7)"></div>
    <div class="listing-body">
      <h3 class="listing-title">Johnson Apartment</h3>
      <p class="location"><b>Location :</b> New Jersey | USA</p>
      <div class="listing-actions"><div class="people-pill">People Accomodated : <span>10</span></div><div class="icon-btn"><svg viewBox="0 0 13 13"><path d="M6.5 11L2 6.5a2.5 2.5 0 0 1 4.5-3 2.5 2.5 0 0 1 4.5 3z" fill="#fff"/></svg></div><div class="icon-btn light"><svg viewBox="0 0 13 13"><path d="M2 7l4 4 5-9" stroke="#fff" stroke-width="2" fill="none"/></svg></div></div>
      <div class="dash"></div>
      <p class="excerpt">Lorem ipsum dolor sit amet, consectetur adipiscing elit, sed do eiusmod tempor incididunt ut labore et dolore magna aliqua. Ut enim ad minim veniam, quis nostrud exercitation.</p>
      <p class="price">PRICE : $1,65,000</p>
      <span class="tag-btn">View location</span>
      <div class="dash"></div>
      <div class="amenity-row">
        <span><svg viewBox="0 0 18 14" fill="none" stroke="#999" stroke-width="1.5"><rect x="1" y="1" width="16" height="10"/><path d="M6 7a4 4 0 0 1 6 0"/></svg>Super-fast wifi</span>
        <span><svg viewBox="0 0 18 14" fill="none" stroke="#999" stroke-width="1.5"><path d="M1 2v11M1 9h16v4M1 6h16v3"/></svg>Comfy beds</span>
        <span><svg viewBox="0 0 18 14" fill="none" stroke="#999" stroke-width="1.5"><path d="M3 6h12v6H3zM1 6h16"/></svg>Full kitchen</span>
        <span><svg viewBox="0 0 18 14" fill="none" stroke="#999" stroke-width="1.5"><path d="M4 7V2h10v5M2 7h14v4H2z"/></svg>Furniture</span>
      </div>
    </div>
  </article>

  <div class="more-btn">View more properties</div>
</section>

<section class="video-band" role="img" aria-label="Background photo of a dim hotel-style bedroom">
  <div class="video-frame" role="img" aria-label="Video still of a bedroom with purple headboard">
    <p>Welcome to the<br>Revolution</p>
    <svg class="play" viewBox="0 0 60 60"><circle cx="30" cy="30" r="28" fill="rgba(255,255,255,.35)"/><path d="M24 18l18 12-18 12z" fill="#fff"/></svg>
  </div>
</section>

<section class="featured">
  <h2 class="section-title">Featured Accommodations</h2>

  <article class="feature-card" style="top:189px;left:143px">
    <div class="feature-photo" role="img" aria-label="Photo of a cosy bedroom with warm lamps" style="background:linear-gradient(135deg,#6b4c34,#a47d5a 55%,#d9c3a4)"><div class="icons"><div class="icon-btn"><svg viewBox="0 0 13 13"><path d="M6.5 11L2 6.5a2.5 2.5 0 0 1 4.5-3 2.5 2.5 0 0 1 4.5 3z" fill="#fff"/></svg></div><div class="icon-btn light"><svg viewBox="0 0 13 13"><path d="M2 7l4 4 5-9" stroke="#fff" stroke-width="2" fill="none"/></svg></div></div></div>
    <div class="feature-body"><h3 class="listing-title">Johnson Apartment</h3><p class="location"><b>Location :</b> New Jersey | USA</p><p class="excerpt">Lorem ipsum dolor sit amet, consectetur adipiscing elit, sed do eiusmod tempor incididunt ut labore.</p><span class="tag-btn">View location</span><p class="price">PRICE : $25,000</p><span class="details-btn">View details</span></div>
  </article>

  <article class="feature-card" style="top:189px;left:455px">
    <div class="feature-photo" role="img" aria-label="Photo of a bedroom with brick wall and pastel bedding" style="background:linear-gradient(135deg,#9b6b55,#c9a9a3 55%,#e6dcd8)"><div class="icons"><div class="icon-btn"><svg viewBox="0 0 13 13"><path d="M6.5 11L2 6.5a2.5 2.5 0 0 1 4.5-3 2.5 2.5 0 0 1 4.5 3z" fill="#fff"/></svg></div><div class="icon-btn light"><svg viewBox="0 0 13 13"><path d="M2 7l4 4 5-9" stroke="#fff" stroke-width="2" fill="none"/></svg></div></div></div>
    <div class="feature-body"><h3 class="listing-title">Johnson Apartment</h3><p class="location"><b>Location :</b> New Jersey | USA</p><p class="excerpt">Lorem ipsum dolor sit amet, consectetur adipiscing elit, sed do eiusmod tempor incididunt ut labore.</p><span class="tag-btn">View location</span><p class="price">PRICE : $15,000</p><span class="details-btn">View details</span></div>
  </article>

  <article class="feature-card" style="top:189px;left:767px">
    <div class="feature-photo" role="img" aria-label="Photo of a grey bedroom with tufted headboard" style="background:linear-gradient(135deg,#cfcac4,#8f8983 55%,#ece8e2)"><div class="icons"><div class="icon-btn"><svg viewBox="0 0 13 13"><path d="M6.5 11L2 6.5a2.5 2.5 0 0 1 4.5-3 2.5 2.5 0 0 1 4.5 3z" fill="#fff"/></svg></div><div class="icon-btn light"><svg viewBox="0 0 13 13"><path d="M2 7l4 4 5-9" stroke="#fff" stroke-width="2" fill="none"/></svg></div></div></div>
    <div class="feature-body"><h3 class="listing-title">Johnson Apartment</h3><p class="location"><b>Location :</b> New Jersey | USA</p><p class="excerpt">Lorem ipsum dolor sit amet, consectetur adipiscing elit, sed do eiusmod tempor incididunt ut labore.</p><span class="tag-btn">View location</span><p class="price">PRICE : $45,000</p><span class="details-btn">View details</span></div>
  </article>

  <article class="feature-card" style="top:722px;left:143px">
    <div class="feature-photo" role="img" aria-label="Photo of a bedroom with dark feature wall" style="background:linear-gradient(135deg,#2f3033,#6a6764 55%,#d8d4cf)"><div class="icons"><div class="icon-btn"><svg viewBox="0 0 13 13"><path d="M6.5 11L2 6.5a2.5 2.5 0 0 1 4.5-3 2.5 2.5 0 0 1 4.5 3z" fill="#fff"/></svg></div><div class="icon-btn light"><svg viewBox="0 0 13 13"><path d="M2 7l4 4 5-9" stroke="#fff" stroke-width="2" fill="none"/></svg></div></div></div>
    <div class="feature-body"><h3 class="listing-title">Johnson Apartment</h3><p class="location"><b>Location :</b> New Jersey | USA</p><p class="excerpt">Lorem ipsum dolor sit amet, consectetur adipiscing elit, sed do eiusmod tempor incididunt ut labore.</p><span class="tag-btn">View location</span><p class="price">PRICE : $65,000</p><span class="details-btn">View details</span></div>
  </article>

  <article class="feature-card" style="top:722px;left:455px">
    <div class="feature-photo" role="img" aria-label="Photo of a bedroom with red bedding" style="background:linear-gradient(135deg,#e8e4dd,#b3262a 55%,#5c2a26)"><div class="icons"><div class="icon-btn"><svg viewBox="0 0 13 13"><path d="M6.5 11L2 6.5a2.5 2.5 0 0 1 4.5-3 2.5 2.5 0 0 1 4.5 3z" fill="#fff"/></svg></div><div class="icon-btn light"><svg viewBox="0 0 13 13"><path d="M2 7l4 4 5-9" stroke="#fff" stroke-width="2" fill="none"/></svg></div></div></div>
    <div class="feature-body"><h3 class="listing-title">Johnson Apartment</h3><p class="location"><b>Location :</b> New Jersey | USA</p><p class="excerpt">Lorem ipsum dolor sit amet, consectetur adipiscing elit, sed do eiusmod tempor incididunt ut labore.</p><span class="tag-btn">View location</span><p class="price">PRICE : $95,000</p><span class="details-btn">View details</span></div>
  </article>

  <article class="feature-card" style="top:722px;left:767px">
    <div class="feature-photo" role="img" aria-label="Photo of a bedroom with large windows and warm light" style="background:linear-gradient(135deg,#8a7761,#5a4a3c 50%,#c8b59a)"><div class="icons"><div class="icon-btn"><svg viewBox="0 0 13 13"><path d="M6.5 11L2 6.5a2.5 2.5 0 0 1 4.5-3 2.5 2.5 0 0 1 4.5 3z" fill="#fff"/></svg></div><div class="icon-btn light"><svg viewBox="0 0 13 13"><path d="M2 7l4 4 5-9" stroke="#fff" stroke-width="2" fill="none"/></svg></div></div></div>
    <div class="feature-body"><h3 class="listing-title">Johnson Apartment</h3><p class="location"><b>Location :</b> New Jersey | USA</p><p class="excerpt">Lorem ipsum dolor sit amet, consectetur adipiscing elit, sed do eiusmod tempor incididunt ut labore.</p><span class="tag-btn">View location</span><p class="price">PRICE : $19,000</p><span class="details-btn">View details</span></div>
  </article>

  <div class="scroll-down"><svg width="16" height="10" viewBox="0 0 16 10"><path d="M2 2l6 6 6-6" stroke="#666" stroke-width="2" fill="none"/></svg></div>
</section>

<section class="testimonials">
  <h2 class="section-title">Testimonials</h2>
  <div class="guest-photo" role="img" aria-label="Photo of a house exterior at dusk"></div>
  <p class="quote">Quick, friendly replies before arrival and a smooth self check-in. The flat was spotless, the bed was so comfy and the kitchen had all I needed.</p>
  <div class="guest"><strong>Guest Review, Alder Court,</strong><span>Kelmouth</span></div>
</section>

<footer class="site-footer">
  <div class="footer-col footer-about">
    <span class="brand-name">Bright Nest</span>
    <p>We founded Bright Nest Serviced Apartments as property owners and investors ourselves, who were unable to source a managing agent specialising in the operation of Serviced Accommodation.</p>
    <span class="read-more">Read more</span>
  </div>
  <div class="footer-col footer-links">
    <h4>Quick Links</h4>
    <p>Home<br>About Us<br>Accomodation<br>Our Customers<br>Contact Us</p>
  </div>
  <div class="footer-col footer-links">
    <h4>Other Links</h4>
    <p>Careers<br>Gift Cards<br>Contact Us<br>Privacy Policy<br>Terms of Use</p>
  </div>
  <div class="footer-col footer-contact">
    <h4>Contact Us</h4>
    <div class="contact-line"><svg viewBox="0 0 13 13"><path d="M6.5 12S2 7.5 2 5a4.5 4.5 0 0 1 9 0c0 2.5-4.5 7-4.5 7z" fill="#fff"/><circle cx="6.5" cy="5" r="1.6" fill="#a6985f"/></svg><span>Corran House<br>12 Mill Lane<br>Fenbridge</span></div>
    <div class="contact-line"><svg viewBox="0 0 13 13"><path d="M3 1l2 3-1.5 1.5a7 7 0 0 0 4 4L9 8l3 2-1 2c-5 0-10-5-10-10z" fill="#fff"/></svg><span>1-800-204-7731</span></div>
    <div class="contact-line"><svg viewBox="0 0 13 13"><rect x="1" y="3" width="11" height="8" fill="none" stroke="#fff"/><path d="M1 3l5.5 4.5L12 3" stroke="#fff" fill="none"/></svg><span>E-Mail: hello@brightnest-example.com</span></div>
  </div>
</footer>

<section class="bottom-bar">
  <span>© 2017 COMPANY NAME &nbsp;|&nbsp; ALL RIGHTS RESERVED</span>
  <div class="socials"><i></i><i></i><i></i><i></i></div>
</section>

</body>
</html>
```